Marketplace Lending Diagram

I need a diagram drawn of how our marketplace works that will be part of an article posted by a New York publisher.

The diagrams needs to depict the current state of the market and how our company Borrowix is creating a new market.

Our website is here to give you some more information.
http://www.borrowix-example.com/

There is a video on the website explaining further how this new market works

The attached file needs to be re-drawn using Adobe Illustrator and with a more professional style.

The deliverables need to be an AI file, and PNG file of 300 dpi.

Thanks.

Target Market(s)

Financial community - bankers, hedge fund managers, high net worth individuals

Industry/Entity Type

It Company

Font styles to use
Sans Serif

Requirements
Must have
• 1. Title needs to be "Disintermediating Commercial Mortgage Backed Securitization (CMBS)'
• 2. Change 'Before' and 'After' to 'Current Lending' and 'Marketplace Lending'
• 3. Show the flow from Package to Tranche as the creation of CMBS products. Maybe show an extra dotted arrow with a 'CMBS' label?
• 4. The 'Package' picture look should look like a 3D box to symbolise a pooling of loans.
• 5. Between 'Super Fund' and 'Investors' can this look like three 3D packages instead of money. This symbolise different products being sold to investors.
• 6. Rename 'Super Fund' to 'Mutual Fund'.
• 7. The borrower should symbolise a corporation owning a $10m building. Make the borrower look like a business owner. Need a picture of an office building with the words 'collatoral property'
• See this for an example:
• http://www.quelvane.example.jp/servicer/e/service/cmbs.htm
• 8. 'Super Fund' should be a picture of a little plant growing from gold coins:
• http://www.tormeddi-am.example/faqs/images/fundinvestrimg.gif

```html
<!DOCTYPE html>
<html lang="en">
<head>
<meta charset="utf-8">
<title>Disintermediating CMBS – Marketplace Lending Diagram</title>
<link rel="stylesheet" href="https://fonts.googleapis.com/css2?family=Francois+One&family=Oswald:wght@600;700&display=swap">
<style>
  :root{
    --orange:#ef6a36;
    --teal:#178a80;
    --teal-soft:#2aa195;
    --teal-light:#5fbdb3;
    --title-ink:#dce6e4;
    --paper:#ffffff;
    --label-ink:#ffffff;
  }
  *{margin:0;padding:0;box-sizing:border-box}
  html,body{width:1200px;height:1000px;overflow:hidden;background:var(--paper)}
  .canvas{position:relative;width:1200px;height:1000px;background:var(--paper);overflow:hidden}
  .diagram-frame{position:absolute;left:18px;top:36px;width:1164px;height:928px;border:3px solid var(--teal)}
  .connectors{position:absolute;left:0;top:0;width:1200px;height:1000px}
  .title-banner{position:absolute;left:222px;top:62px;width:758px;height:118px;background:var(--teal);border-radius:14px;
    display:flex;align-items:center;justify-content:center;text-align:center;
    font-family:"Oswald",sans-serif;font-weight:700;font-size:37px;line-height:1.15;letter-spacing:1px;color:var(--title-ink)}
  .section-heading{position:absolute;top:254px;font-family:"Francois One",sans-serif;font-weight:400;font-size:42px;color:var(--orange);letter-spacing:.5px;white-space:nowrap}
  .section-heading.current{left:200px}
  .section-heading.marketplace{left:735px}
  .step-label{position:absolute;height:44px;background:var(--orange);border-radius:7px;color:var(--label-ink);
    font-family:"Francois One",sans-serif;font-size:30px;letter-spacing:.5px;white-space:nowrap;
    display:flex;align-items:center;justify-content:center;line-height:1}
  .step-label.stacked{height:100px;flex-direction:column;font-size:29px;line-height:1.15}
  .tranche-letter{position:absolute;font-family:"Oswald",sans-serif;font-weight:600;font-size:17px;color:var(--orange)}
</style>
</head>
<body>
<main class="canvas">
  <div class="diagram-frame"></div>

  <svg class="connectors" viewBox="0 0 1200 1000">
    <defs>
      <linearGradient id="figure-fill" x1="0" y1="0" x2="0" y2="1">
        <stop offset="0" stop-color="var(--teal-soft)"/>
        <stop offset="1" stop-color="var(--teal)"/>
      </linearGradient>
      <symbol id="package-icon" viewBox="0 0 40 36">
        <rect x="3" y="13" width="34" height="21" fill="var(--teal)"/>
        <polygon points="3,13 13,4 22,13" fill="var(--teal-soft)"/>
        <polygon points="37,13 27,4 18,13" fill="var(--teal-light)"/>
        <line x1="20" y1="13" x2="20" y2="34" stroke="#fff" stroke-width="1.5"/>
      </symbol>
    </defs>

    <g class="dotted-links" fill="none" stroke="var(--teal)" stroke-width="2.5" stroke-dasharray="4 4">
      <line x1="215" y1="398" x2="250" y2="398"/>
      <line x1="357" y1="398" x2="385" y2="398"/>
      <line x1="483" y1="398" x2="518" y2="398"/>
      <polyline points="670,398 692,398 692,648 672,648"/>
      <line x1="466" y1="648" x2="493" y2="648"/>
      <polyline points="306,648 250,648 161,812"/>
      <line x1="161" y1="864" x2="200" y2="864"/>
    </g>

    <!-- Borrower (current lending) -->
    <rect x="63" y="447" width="124" height="228" rx="40" fill="url(#figure-fill)" role="img" aria-label="Business owner borrower holding a briefcase"/>

    <!-- Apply: application form with pencil -->
    <g class="icon-application" fill="none" stroke="var(--teal)" stroke-width="4">
      <rect x="260" y="470" width="56" height="84" rx="3"/>
      <line x1="270" y1="492" x2="306" y2="492"/>
      <line x1="270" y1="506" x2="306" y2="506"/>
      <line x1="270" y1="520" x2="306" y2="520"/>
      <line x1="270" y1="534" x2="296" y2="534"/>
    </g>
    <g class="icon-pencil">
      <rect x="322" y="470" width="12" height="72" fill="var(--orange)"/>
      <polygon points="322,542 334,542 328,560" fill="var(--orange)"/>
    </g>

    <!-- Bank -->
    <g class="icon-bank" fill="var(--teal)">
      <polygon points="435,466 388,490 482,490"/>
      <rect x="392" y="493" width="87" height="6"/>
      <rect x="399" y="503" width="11" height="40"/>
      <rect x="419" y="503" width="11" height="40"/>
      <rect x="441" y="503" width="11" height="40"/>
      <rect x="461" y="503" width="11" height="40"/>
      <rect x="392" y="546" width="87" height="7"/>
      <rect x="386" y="555" width="99" height="6"/>
    </g>

    <!-- Package: open 3D box -->
    <g class="icon-package">
      <rect x="554" y="500" width="84" height="60" fill="var(--teal)"/>
      <polygon points="554,500 540,478 590,470 596,494" fill="var(--teal-soft)"/>
      <polygon points="638,500 652,478 602,470 596,494" fill="var(--teal-light)"/>
      <line x1="596" y1="500" x2="596" y2="560" stroke="#fff" stroke-width="2"/>
      <path d="M616 548v-16m-6 6l6-6 6 6" fill="none" stroke="#fff" stroke-width="2.5"/>
    </g>

    <!-- Small packages toward mutual fund -->
    <use href="#package-icon" x="185" y="604" width="40" height="36"/>
    <use href="#package-icon" x="133" y="676" width="40" height="36"/>
    <use href="#package-icon" x="75" y="738" width="44" height="40"/>

    <!-- Tranche documents A B C -->
    <g class="icon-tranche-docs" fill="none" stroke="var(--teal)" stroke-width="3.5">
      <rect x="316" y="704" width="40" height="72" rx="2"/>
      <rect x="368" y="704" width="40" height="72" rx="2"/>
      <rect x="420" y="704" width="40" height="72" rx="2"/>
      <path d="M324 722h24M324 734h24M324 746h24M324 758h16"/>
      <path d="M376 722h24M376 734h24M376 746h24M376 758h16"/>
      <path d="M428 722h24M428 734h24M428 746h24M428 758h16"/>
    </g>

    <!-- Securitised document with lock -->
    <g class="icon-secured-doc" fill="none" stroke="var(--teal)" stroke-width="4">
      <rect x="553" y="703" width="62" height="98" rx="3"/>
      <path d="M564 726h40M564 742h40M564 758h40M564 774h26"/>
    </g>
    <circle cx="612" cy="806" r="26" fill="var(--orange)"/>
    <g class="icon-lock" fill="none" stroke="#fff" stroke-width="3">
      <rect x="606" y="804" width="18" height="14" rx="2" fill="#fff"/>
      <path d="M609 804v-6a6 6 0 0 1 12 0v6"/>
      <circle cx="596" cy="811" r="5"/>
      <line x1="601" y1="811" x2="606" y2="811"/>
    </g>

    <!-- Investors groups -->
    <rect x="378" y="815" width="91" height="122" rx="30" fill="url(#figure-fill)" role="img" aria-label="Group of three investors"/>
    <rect x="960" y="692" width="97" height="149" rx="30" fill="url(#figure-fill)" role="img" aria-label="Group of three investors"/>

    <!-- Marketplace lending -->
    <rect x="852" y="465" width="78" height="140" rx="26" fill="url(#figure-fill)" role="img" aria-label="Business owner borrower holding a briefcase"/>
    <g class="two-way-arrows" stroke="var(--teal)" stroke-width="3" fill="var(--teal)">
      <line x1="945" y1="432" x2="945" y2="616"/>
      <polygon points="939,434 951,434 945,422" stroke="none"/>
      <polygon points="939,614 951,614 945,626" stroke="none"/>
      <line x1="945" y1="684" x2="945" y2="864"/>
      <polygon points="939,686 951,686 945,674" stroke="none"/>
      <polygon points="939,862 951,862 945,874" stroke="none"/>
    </g>
  </svg>

  <h1 class="title-banner">DISINTERMEDIATING COMMERCIAL MORTGAGE<br>BACKED SECURITIZATION (CMBS)</h1>

  <h2 class="section-heading current">CURRENT LENDING</h2>
  <h2 class="section-heading marketplace">MARKETPLACE LENDING</h2>

  <div class="step-label" style="left:33px;top:376px;width:182px">BORROWER</div>
  <div class="step-label" style="left:250px;top:376px;width:107px">APPLY</div>
  <div class="step-label" style="left:385px;top:376px;width:98px">BANK</div>
  <div class="step-label" style="left:518px;top:376px;width:152px">PACKAGE</div>
  <div class="step-label" style="left:306px;top:626px;width:160px">TRANCHE</div>
  <div class="step-label" style="left:493px;top:626px;width:179px">SECURITISE</div>
  <div class="step-label stacked" style="left:38px;top:812px;width:123px"><span>MUTUAL</span><span>FUND</span></div>
  <div class="step-label" style="left:200px;top:842px;width:172px">INVESTORS</div>

  <span class="tranche-letter" style="left:330px;top:782px">A</span>
  <span class="tranche-letter" style="left:382px;top:782px">B</span>
  <span class="tranche-letter" style="left:434px;top:782px">C</span>

  <div class="step-label" style="left:852px;top:376px;width:182px">BORROWER</div>
  <div class="step-label" style="left:915px;top:626px;width:62px">BRX</div>
  <div class="step-label" style="left:852px;top:876px;width:182px">INVESTORS</div>
</main>
</body>
</html>
```